"End of year wishes" - Electronic card

Velmora is a regulatory consulting company in the cosmetic sector. We provide premium services and have 12 years of experience.
Please visit our website for more information: https://velmora-example.com
Like every year, we would like to send an electronic design to our clients and partners to wish them happy holidays. This year, we would like to share two good news with them: offer them a surprise (to be revealed later on) and invite them to visit our new brand new website. We relay on your talent and imagination for the design! We need something very professional, serious, beautiful and in line with our graphic layout (see our company website)

Target Market(s)

cosmetic brands

Industry/Entity Type

Cosmetics

Requirements
Must have
• The following statement should be included to the design:

We wish you a Happy Holiday and a Marvelous New Year 2021!
As December is the month of giving, we have a surprise for you. Please contact your dedicated Account Manager to find out more!

Good news never comes alone, we've also updated our website in order to serve you better. We hope you like it as much as we do.
Please enjoy the experience: www.velmora-example.com

```html
<!DOCTYPE html>
<html lang="en">
<head>
<meta charset="UTF-8">
<title>Velmora – Season's Greetings 2021</title>
<link rel="stylesheet" href="https://fonts.googleapis.com/css2?family=Great+Vibes&family=Montserrat:wght@600;700&display=swap">
<style>
  :root {
    --panel: #1f2a35;
    --accent: #8fcc0a;
    --photo-light: #f6f7f8;
    --photo-mid: #e9ebed;
  }
  * { margin: 0; padding: 0; box-sizing: border-box; }
  html, body { width: 1200px; height: 852px; overflow: hidden; background: var(--panel); }
  .card { position: relative; width: 1200px; height: 852px; }
  .gift-photo {
    position: absolute; left: 0; top: 0; width: 563px; height: 852px;
    background: radial-gradient(ellipse at 40% 45%, var(--photo-mid) 0%, var(--photo-light) 60%);
  }
  .message-panel {
    position: absolute; left: 563px; top: 0; width: 637px; height: 852px;
    background: var(--panel);
  }
  .frame {
    position: absolute; left: 19px; top: 20px; width: 597px; height: 811px;
    border: 3px solid var(--accent);
  }
  .rule {
    position: absolute; left: 255px; width: 127px; height: 8px;
    border-top: 3px solid var(--accent); border-bottom: 3px solid var(--accent);
  }
  .rule--top { top: 159px; }
  .rule--bottom { top: 693px; }
  .text {
    position: absolute; left: 0; width: 637px; text-align: center;
    color: var(--accent); font-family: "Montserrat", sans-serif;
  }
  .kicker {
    top: 205px; font-size: 16px; font-weight: 700; letter-spacing: 1.6px;
  }
  .headline {
    top: 258px; font-family: "Great Vibes", cursive; font-size: 88px;
    line-height: 104px; font-weight: 400;
  }
  .body {
    font-size: 16px; font-weight: 700; line-height: 22px;
    left: 60px; width: 517px;
  }
  .body--surprise { top: 525px; }
  .body--website { top: 611px; }
  .call-to-action {
    top: 717px; font-size: 16.5px; font-weight: 700; letter-spacing: 1.4px; line-height: 22px;
  }
</style>
</head>
<body>
  <main class="card">
    <div class="gift-photo" role="img" aria-label="Photo of a grey book wrapped with a red satin ribbon, a lit tealight candle and sprigs of thyme on a white surface"></div>
    <section class="message-panel">
      <div class="frame"></div>
      <div class="rule rule--top"></div>
      <p class="text kicker">WE WISH YOU A HAPPY HOLIDAY AND A</p>
      <h1 class="text headline">Marvelous New<br>Year 2021!</h1>
      <p class="text body body--surprise">As December is the month of giving, we have a surprise for you. Please contact your dedicated Account Manager to find out more</p>
      <p class="text body body--website">Good news never comes alone, we've also updated our website in order to serve you better. We hope you like it as much as we do.</p>
      <div class="rule rule--bottom"></div>
      <p class="text call-to-action">PLEASE ENJOY THE EXPERIENCE:<br>WWW.VELMORA-EXAMPLE.COM</p>
    </section>
  </main>
</body>
</html>
```